Flyer-Design für Kreativwerkstatt
Zielgruppe
Kreativwerkstatt für Touristen - vorrangig Frauen
Aufgabenstellung
1 mal gefaltet
Wenn möglich außer dem Logo noch folgenden Text verwenden
Kreativität fängt da ,wo der Verstand aufhört das denken zu behindern

```html
<!DOCTYPE html>
<html lang="de">
<head>
<meta charset="utf-8">
<title>Lindenstube – Kreativwerkstatt Flyer</title>
<link rel="stylesheet" href="https://fonts.googleapis.com/css2?family=Jost:wght@300;400&family=Parisienne&display=swap">
<style>
  :root {
    --stage: #6f4f39;
    --orange-deep: #d4620f;
    --orange-mid: #e8821f;
    --orange-light: #f2a23a;
    --cream: #fdf0dc;
    --ink-light: #fff4e4;
    --cutout: #5a3f2e;
    --cutout-light: #86705f;
    --map-base: #e6e4df;
    --map-green: #bfe0b4;
  }
  html, body {
    margin: 0;
    width: 1200px;
    height: 864px;
    overflow: hidden;
    background: var(--stage);
  }
  .flyer {
    position: absolute;
    left: 230px;
    top: 52px;
    width: 740px;
    height: 760px;
    display: flex;
    box-shadow: 0 18px 40px rgba(0,0,0,0.35);
  }
  .panel {
    position: relative;
    width: 370px;
    height: 760px;
    background: linear-gradient(160deg, var(--orange-light) 0%, var(--orange-mid) 45%, var(--orange-deep) 100%);
    color: var(--ink-light);
    font-family: "Jost", sans-serif;
    font-weight: 300;
  }
  .panel--cover {
    background: linear-gradient(200deg, var(--orange-light) 0%, var(--orange-mid) 40%, var(--orange-deep) 100%);
    border-left: 1px solid rgba(160,60,0,0.45);
  }
  .brand {
    position: absolute;
    top: 92px;
    left: 0;
    right: 0;
    text-align: center;
    font-size: 44px;
    font-weight: 400;
    letter-spacing: 1px;
    color: var(--cream);
    margin: 0;
  }
  .directions-title {
    position: absolute;
    top: 232px;
    left: 0;
    right: 0;
    text-align: center;
    font-size: 21px;
    letter-spacing: 2px;
    margin: 0;
  }
  .map-area {
    position: absolute;
    top: 284px;
    left: 28px;
    width: 314px;
    height: 236px;
    background: radial-gradient(ellipse at 30% 40%, var(--map-green) 0%, var(--map-base) 55%);
  }
  .address {
    position: absolute;
    left: 40px;
    bottom: 56px;
    font-size: 15.5px;
    line-height: 1.45;
    letter-spacing: 1.2px;
    font-style: normal;
  }
  .cutout {
    position: absolute;
    top: 70px;
    left: 40px;
  }
  .motto {
    position: absolute;
    top: 350px;
    left: 0;
    right: 0;
    text-align: center;
    font-family: "Parisienne", cursive;
    font-size: 34px;
    line-height: 1.35;
    margin: 0;
    color: var(--ink-light);
  }
  .motto-art {
    position: absolute;
    top: 540px;
    left: 60px;
    width: 250px;
    height: 180px;
    border-radius: 40%;
    background: radial-gradient(ellipse, rgba(190,80,10,0.35) 0%, rgba(190,80,10,0) 70%);
  }
</style>
</head>
<body>
  <main class="flyer">
    <section class="panel panel--back">
      <h1 class="brand">Lindenstube</h1>
      <h2 class="directions-title">So können Sie uns finden…</h2>
      <div class="map-area" role="img" aria-label="Straßenkarte der Umgebung mit Seen, Wäldern und Anfahrtsweg zur Werkstatt"></div>
      <address class="address">
        Lindenstube<br>
        Maren Kolbitz<br>
        Wiesenweg 7<br>
        17099 Neudorf / Am Hofe<br>
        Tel. 03991 / 24 65 80<br>
        www.lindenstube-werkstatt.de
      </address>
    </section>
    <section class="panel panel--cover">
      <svg class="cutout" width="290" height="220" viewBox="0 0 290 220" aria-hidden="true">
        <defs>
          <linearGradient id="cutoutShade" x1="0" y1="0" x2="1" y2="1">
            <stop offset="0" stop-color="var(--cutout)"/>
            <stop offset="1" stop-color="var(--cutout-light)"/>
          </linearGradient>
        </defs>
        <ellipse cx="145" cy="110" rx="143" ry="108" fill="url(#cutoutShade)"/>
      </svg>
      <p class="motto">Kreativität fängt da an,<br>wo der Verstand aufhört<br>das Denken zu behindern</p>
      <div class="motto-art" role="img" aria-label="Zart eingeblendetes aufgeschlagenes Buch, aus dem Schmetterlinge aufsteigen"></div>
    </section>
  </main>
</body>
</html>
```